Accountant & CPA Website $100 bonus

We are designing a website for our client Tallow Ridge Accountants and CPAs. They are a new business and looking for a clean, modern website. The services they offer are siilar to: https://www.dvm-lqt.com/index.htm

We would like to see designs that use the black and the green mostly, with a hint of purple and grey. However, we do like to give our designers the freedom to be creative. If you see a different vison, feel free to express that.

Number of Pages Required

1 page

Font styles to use
Sans Serif

```html
<!DOCTYPE html>
<html lang="en">
<head>
<meta charset="utf-8">
<title>Tallow Ridge Accountants &amp; CPAs</title>
<link rel="stylesheet" href="https://fonts.googleapis.com/css2?family=Oswald:wght@300;400;500;600&family=Roboto:wght@400;500&display=swap">
<style>
:root{
  --green:#76931f;
  --green-dark:#5f7a14;
  --purple:#2f1690;
  --black:#000;
  --white:#fff;
  --grey:#6f6f6f;
  --footer:#76931f;
}
*{margin:0;padding:0;box-sizing:border-box}
html,body{width:1200px;height:2966px;overflow:hidden;background:var(--black)}
body{position:relative;font-family:'Roboto',sans-serif;color:var(--white)}
.abs{position:absolute}

/* header */
.site-header{left:0;top:0;width:1200px;height:115px;background:var(--black)}
.brand{left:113px;top:30px;display:flex;align-items:center;gap:12px}
.brand-dot{width:22px;height:22px;border-radius:50%;background:var(--purple)}
.brand-name{font-family:'Oswald',sans-serif;font-weight:500;font-size:42px;line-height:1;color:var(--green);letter-spacing:1px}
.nav a{position:absolute;top:46px;font-size:15px;color:var(--white);text-decoration:none;letter-spacing:.2px}
.nav a.active{color:var(--purple)}
.nav a.active::after{content:"";position:absolute;left:0;right:0;bottom:-6px;height:2px;background:var(--purple)}
.btn{position:absolute;display:flex;align-items:center;justify-content:center;border-radius:24px;font-family:'Oswald',sans-serif;font-weight:500;font-size:16px;color:var(--white);text-transform:uppercase}
.btn-login{left:986px;top:32px;width:102px;height:45px;background:var(--green)}

/* hero */
.hero{left:0;top:115px;width:1200px;height:599px;background:linear-gradient(90deg,#6e8a3a 0%,#8ea65a 35%,#c9c2b3 55%,#b33a36 70%,#d8d8dc 100%)}
.hero-welcome{left:109px;top:252px;font-family:'Oswald',sans-serif;font-weight:300;font-size:46px;color:var(--white)}
.hero-title{left:109px;top:318px;font-family:'Oswald',sans-serif;font-weight:600;font-size:62px;line-height:74px;color:var(--white)}
.hero-title .accent{color:var(--purple)}
.btn-start{left:109px;top:497px;width:124px;height:44px;background:var(--purple)}
.slider-dots{left:568px;top:670px;display:flex;gap:7px}
.slider-dots span{width:11px;height:11px;border-radius:50%;background:#555}
.slider-dots span.on{background:var(--purple)}

/* about */
.about{left:0;top:714px;width:1200px;height:582px;background:var(--black)}
.about-visual{left:181px;top:800px;width:309px;height:409px;border-radius:30px;background:linear-gradient(160deg,#1d2333,#5a6a86 55%,#c9d3e0)}
.section-title{font-family:'Oswald',sans-serif;font-weight:500;font-size:39px;color:var(--green);letter-spacing:.5px}
.section-title::after{content:"";display:inline-block;width:10px;height:10px;border-radius:50%;background:var(--purple);margin-left:10px}
.about-title{left:603px;top:790px}
.about-text{left:603px;top:874px;width:485px;font-size:15.3px;line-height:25.8px;text-align:justify}
.btn-learn{left:603px;top:1165px;width:124px;height:44px;background:var(--green)}

/* services */
.services{left:0;top:1296px;width:1200px;height:599px;background:linear-gradient(120deg,#7d7d7d,#6a6a6a 50%,#767676)}
.services-title{left:0;width:1200px;top:1365px;text-align:center}
.service{position:absolute;width:440px;height:180px}
.service-icon{position:absolute;left:0;top:0;width:106px;height:106px;border-radius:50%;border:4px solid var(--green);display:flex;align-items:center;justify-content:center}
.service-icon .inner{width:84px;height:84px;border-radius:50%;background:var(--white);display:flex;align-items:center;justify-content:center}
.service h3{position:absolute;left:130px;top:-8px;font-family:'Oswald',sans-serif;font-weight:400;font-size:24px;color:var(--white)}
.service p{position:absolute;left:132px;top:40px;width:314px;font-size:15px;line-height:26.5px}
.service .more{position:absolute;left:132px;top:140px;font-family:'Oswald',sans-serif;font-size:17px;color:var(--green);text-decoration:underline}

/* blog */
.blog{left:0;top:1895px;width:1200px;height:661px;background:var(--black)}
.blog-title{left:0;width:1200px;top:1970px;text-align:center}
.post{position:absolute;top:2059px;width:313px}
.post-img{width:313px;height:229px}
.post h3{margin-top:20px;font-family:'Oswald',sans-serif;font-weight:400;font-size:24px;line-height:32px}
.post p{margin-top:12px;font-size:16px;line-height:26px}
.post .more{display:block;margin-top:12px;font-family:'Oswald',sans-serif;font-size:16px;color:var(--green)}

/* footer */
.site-footer{left:0;top:2556px;width:1200px;height:410px;background:var(--footer)}
.foot-brand{left:113px;top:2640px;display:flex;align-items:center;gap:14px}
.foot-brand .brand-dot{background:var(--white)}
.foot-brand .brand-name{color:var(--white);font-size:54px}
.contact-line{left:113px;top:2755px;display:flex;align-items:center;gap:14px}
.contact-line .label{font-size:21px;line-height:26px}
.contact-line .phone{font-size:28px;font-weight:500;line-height:32px}
.foot-head{font-size:18px;font-weight:500}
.foot-services{left:531px;top:2626px}
.foot-services ul{list-style:none;margin-top:21px}
.foot-services li{font-size:13.5px;line-height:28px;padding-left:26px;position:relative}
.foot-services li::before{content:"»";position:absolute;left:0;top:-1px}
.newsletter{left:837px;top:2626px;width:251px}
.newsletter p{margin-top:20px;font-size:13px}
.newsletter .field{margin-top:24px;width:251px;height:38px;border-radius:19px;background:var(--white);color:#555;font-size:13px;padding:11px 18px}
.btn-sign{position:static;margin-top:14px;width:112px;height:38px;border-radius:19px;background:var(--purple);font-family:'Roboto',sans-serif;font-size:15px;text-transform:none}
.rule{top:2870px;height:1px;background:rgba(255,255,255,.45)}
.socials{left:500px;top:2848px;display:flex;gap:8px}
.socials span{width:44px;height:44px;border-radius:50%;border:2px solid var(--white)}
.copyright{left:113px;top:2909px;font-size:13px}
.legal{right:115px;top:2909px;font-size:13px}
</style>
</head>
<body>

<header class="abs site-header">
  <div class="abs brand"><span class="brand-dot"></span><span class="brand-name">TALLOW RIDGE</span></div>
  <nav class="nav">
    <a class="active" href="#" style="left:472px">HOME</a>
    <a href="#" style="left:561px">SERVICES</a>
    <a href="#" style="left:676px">ABOUT</a>
    <a href="#" style="left:771px">BLOG</a>
    <a href="#" style="left:856px">CONTACT</a>
  </nav>
  <a class="btn btn-login">Log In</a>
</header>

<section class="abs hero" role="img" aria-label="Hand dropping a coin into a red piggy bank beside stacks of coins and a calculator"></section>
<div class="abs hero-welcome">WELCOME TO</div>
<h1 class="abs hero-title">TALLOW RIDGE <span class="accent">ACCOUNTANTS</span><br>&amp; CPAS</h1>
<a class="btn btn-start">Get Started</a>
<div class="abs slider-dots"><span></span><span></span><span></span><span class="on"></span></div>

<section class="abs about"></section>
<div class="abs about-visual" role="img" aria-label="Photo of hands typing on a calculator keyboard at a desk"></div>
<h2 class="abs section-title about-title">ABOUT US</h2>
<p class="abs about-text">Lorem ipsum dolor sit amet, consectetur adipiscing elit, sed do eiusmod tempor incididunt ut labore et dolore magna aliqua. Ut enim ad minim veniam, quis nostrud exercitation ullamco laboris nisi ut aliquip ex ea commodo consequat. Duis aute irure dolor in reprehenderit in voluptate velit esse cillum dolore eu fugiat nulla pariatur. Excepteur sint occaecat cupidatat non proident, sunt in culpa qui officia deserunt mollit anim id est laborum.Sed ut perspiciatis unde omnis iste natus error sit voluptatem accusantium doloremque laudantium, totam rem aperiam, eaque ipsa quae ab illo inventore veritatis et quasi architecto beatae vitae dicta sunt explicabo.</p>
<a class="btn btn-learn">Learn More</a>

<section class="abs services" role="img" aria-label="Faded photo of an office desk with paperwork behind a grey overlay"></section>
<h2 class="abs section-title services-title">OUR &nbsp;SERVICES</h2>

<div class="service" style="left:120px;top:1465px">
  <div class="service-icon"><div class="inner"><svg width="44" height="44" viewBox="0 0 44 44" fill="none" stroke="#76931f" stroke-width="2"><rect x="8" y="4" width="28" height="36" rx="2"/><line x1="14" y1="14" x2="30" y2="14"/><line x1="14" y1="21" x2="30" y2="21"/><line x1="14" y1="28" x2="24" y2="28"/></svg></div></div>
  <h3>Tax Services</h3>
  <p>Lorem ipsum dolor sit amnsectetur adipiscing elit, sed do eiusmod tempor incididunt ut labore et dolore magna aliqua.</p>
  <a class="more">READ MORE</a>
</div>
<div class="service" style="left:623px;top:1465px">
  <div class="service-icon"><div class="inner"><svg width="44" height="44" viewBox="0 0 44 44" fill="none" stroke="#76931f" stroke-width="2"><circle cx="22" cy="14" r="9"/><path d="M6 34c6-6 12-6 18-3h10"/><line x1="22" y1="9" x2="22" y2="19"/></svg></div></div>
  <h3>Accounting Services</h3>
  <p>Lorem ipsum dolor sit amnsectetur adipiscing elit, sed do eiusmod tempor incididunt ut labore et dolore magna aliqua.</p>
  <a class="more">READ MORE</a>
</div>
<div class="service" style="left:120px;top:1664px">
  <div class="service-icon"><div class="inner"><svg width="44" height="44" viewBox="0 0 44 44" fill="none" stroke="#76931f" stroke-width="2"><path d="M6 38V22l9 5v-5l9 5v-5l9 5V8h5v30z"/><line x1="4" y1="38" x2="40" y2="38"/></svg></div></div>
  <h3>Niche Industries</h3>
  <p>Lorem ipsum dolor sit amnsectetur adipiscing elit, sed do eiusmod tempor incididunt ut labore et dolore magna aliqua.</p>
  <a class="more">READ MORE</a>
</div>
<div class="service" style="left:623px;top:1664px">
  <div class="service-icon"><div class="inner"><svg width="44" height="44" viewBox="0 0 44 44" fill="none" stroke="#76931f" stroke-width="2"><rect x="7" y="5" width="22" height="32" rx="2"/><rect x="22" y="20" width="15" height="19" rx="2"/><line x1="12" y1="12" x2="24" y2="12"/><line x1="12" y1="18" x2="20" y2="18"/><line x1="25" y1="26" x2="34" y2="26"/></svg></div></div>
  <h3>LedgerLine Accounting</h3>
  <p>Lorem ipsum dolor sit amnsectetur adipiscing elit, sed do eiusmod tempor incididunt ut labore et dolore magna aliqua.</p>
  <a class="more">READ MORE</a>
</div>

<section class="abs blog"></section>
<h2 class="abs section-title blog-title">OUR BLOG</h2>

<article class="post" style="left:111px">
  <div class="post-img" role="img" aria-label="Hands reviewing printed financial charts on a desk" style="background:linear-gradient(135deg,#d9dfe6,#8b97a6)"></div>
  <h3>Sed ut perspiciatis unde omnis iste natus error sit</h3>
  <p>Lorem ipsum dolor sit amet, consectetur adipiscing elit, sed do eiusmod tempor</p>
  <a class="more">Read More &rarr;</a>
</article>
<article class="post" style="left:443px">
  <div class="post-img" role="img" aria-label="Business team meeting around a table with laptops" style="background:linear-gradient(135deg,#c7ccd2,#3f4550)"></div>
  <h3>Sed ut perspiciatis unde omnis iste natus error sit</h3>
  <p>Lorem ipsum dolor sit amet, consectetur adipiscing elit, sed do eiusmod tempor</p>
  <a class="more">Read More &rarr;</a>
</article>
<article class="post" style="left:775px">
  <div class="post-img" role="img" aria-label="Person with phone and calculator in front of a laptop showing charts" style="background:linear-gradient(135deg,#e4e8ee,#b49c80)"></div>
  <h3>Sed ut perspiciatis unde omnis iste natus error sit</h3>
  <p>Lorem ipsum dolor sit amet, consectetur adipiscing elit, sed do eiusmod tempor</p>
  <a class="more">Read More &rarr;</a>
</article>

<footer class="abs site-footer"></footer>
<div class="abs foot-brand"><span class="brand-dot"></span><span class="brand-name">TALLOW RIDGE</span></div>
<div class="abs contact-line">
  <svg width="46" height="46" viewBox="0 0 46 46" fill="none" stroke="#fff" stroke-width="2.5"><circle cx="23" cy="23" r="21"/><path d="M15 13l5 0 2 6-3 2c1 3 4 6 7 7l2-3 6 2v5c-10 1-20-9-19-19z" fill="#fff" stroke="none"/></svg>
  <div><div class="label">Contact Us</div><div class="phone">+ 1 555 014 2290</div></div>
</div>
<div class="abs foot-services">
  <div class="foot-head">SERVICES</div>
  <ul><li>Tax Services</li><li>Accounting Services</li><li>Niche Industries</li><li>LedgerLine Accounting</li></ul>
</div>
<div class="abs newsletter">
  <div class="foot-head">SIGN UP NEWSLETTER</div>
  <p>Lorem ipsum dolor sit ameonsectetur adlp</p>
  <div class="field">Enter Email</div>
  <a class="btn btn-sign">SIGN UP</a>
</div>
<div class="abs rule" style="left:113px;width:365px"></div>
<div class="abs rule" style="left:728px;width:360px"></div>
<div class="abs socials" aria-label="Social links"><span></span><span></span><span></span><span></span></div>
<div class="abs copyright">Copyright © 2023 Tallow Ridge Accountants &amp; CPAs. All rights reserved.</div>
<div class="abs legal">Terms of use &nbsp;| &nbsp;Privacy policy &nbsp;| &nbsp;Site map</div>

</body>
</html>
```